Poster promoting the "Golden Crust Day"

The Meridan Federation of Oven Crafts (MFOC) created the "Golden Crust Day" in 2006. It is celebreated each year together with the GNX "Harvest Table Day" on 16th October.
After using different posters for a few years, MFOC decided to settle on a permanent poster some time ago, in order to allow people to recognize the poster long-term.
Now, MFOC feels that this permanent poster needs an update and modernization, apart from including the new MFOC logo.
Requisits:
1. Must include the new MFOC logo
2. The poster should reflect the importance of bread in the world and convey an image of health, innovation and tradition.
3. One version with text, one version without text
4. Text version: one poster for each of the four official MFOC languages:
ENGLISH: Golden Crust Day / 16th October
GERMAN: Goldkrustentag / 16. Oktober
SPANISH: Día de la Corteza Dorada / 16 de Octubre
FRENCH: Journée de la Croûte Dorée / 16 Octobre
5. Colours must be defined with RGB colour code.
MFOC will take a decision regarding the new poster design during the next meeting of its Marketing Commission on March 24th, 2015. Therefore, please submit your proposals by 18th March in order to allow for pre-selection and modification requests.
More about MFOC at www.meridanovencrafts.org.

```html
<!DOCTYPE html>
<html lang="en">
<head>
<meta charset="utf-8">
<title>Golden Crust Day Poster</title>
<link href="https://fonts.googleapis.com/css2?family=Josefin+Sans:wght@600;700&display=swap" rel="stylesheet">
<style>
  :root {
    --page-bg: #e9e8e6;
    --paper: #ffffff;
    --crust-brown: #9e3a17;
    --sky-blue: #74acda;
    --grain-yellow: #f8d200;
    --text-light: #ffffff;
    --loaf-dark: #5a2a16;
    --loaf-mid: #8a4a2c;
    --loaf-flour: #c9b8a8;
  }
  * { margin: 0; padding: 0; box-sizing: border-box; }
  html, body {
    width: 1200px;
    height: 1148px;
    overflow: hidden;
    background: var(--page-bg);
  }
  .poster {
    position: absolute;
    left: 220px;
    top: 36px;
    width: 760px;
    height: 1076px;
    background: var(--paper);
    font-family: "Josefin Sans", sans-serif;
    box-shadow: 0 2px 10px rgba(0,0,0,0.08);
  }
  .brand {
    position: absolute;
    left: 62px;
    top: 92px;
    display: flex;
    align-items: center;
    gap: 14px;
  }
  .brand-dot {
    width: 22px;
    height: 22px;
    border-radius: 50%;
    background: var(--sky-blue);
  }
  .brand-name {
    font-size: 50px;
    font-weight: 700;
    color: var(--crust-brown);
    letter-spacing: 1px;
    line-height: 1;
  }
  .title-block {
    position: absolute;
    left: 14px;
    top: 232px;
    width: 540px;
  }
  .band {
    height: 128px;
    display: flex;
    align-items: center;
    padding-left: 62px;
    color: var(--text-light);
    font-size: 88px;
    font-weight: 700;
    line-height: 1;
    padding-top: 12px;
  }
  .band--brown { background: var(--crust-brown); }
  .band--blue { background: var(--sky-blue); }
  .band--yellow { background: var(--grain-yellow); }
  .band--date {
    background: var(--crust-brown);
    height: 146px;
    font-size: 32px;
    font-weight: 600;
    align-items: flex-start;
    padding-top: 44px;
  }
  .loaf {
    position: absolute;
    left: 356px;
    top: 650px;
    width: 404px;
    height: 400px;
  }
</style>
</head>
<body>
  <main class="poster">
    <div class="brand">
      <span class="brand-name">MFOC</span>
      <span class="brand-dot"></span>
    </div>

    <div class="title-block">
      <h1 class="band band--brown">GOLDEN</h1>
      <div class="band band--blue">CRUST</div>
      <div class="band band--yellow">DAY</div>
      <p class="band band--date">16TH OCTOBER</p>
    </div>

    <svg class="loaf" viewBox="0 0 404 400" role="img" aria-label="Round rustic loaf of bread with a flour-dusted map of the world on its crust">
      <defs>
        <radialGradient id="loafTone" cx="45%" cy="40%" r="60%">
          <stop offset="0%" stop-color="var(--loaf-flour)"/>
          <stop offset="45%" stop-color="var(--loaf-mid)"/>
          <stop offset="100%" stop-color="var(--loaf-dark)"/>
        </radialGradient>
      </defs>
      <ellipse cx="200" cy="196" rx="192" ry="188" fill="url(#loafTone)"/>
    </svg>
  </main>
</body>
</html>
```